Vernalis Medical Business Card

Create a high class Business card for Medical Aesthetics and Wellness Practice called Vernalis Medical Aesthetics and Wellness as per the logo attached.
Addresss is: 412 Harlow Brook Road Suite 318 Ashcombe, New York 11583
Phone (555)294-7051 IG @vernalis_medical
Vernalismedical-example.com

I need 5 different name configurations
1) Dr. Derek Haltsworth
Aesthetics and Wellness Specialist
Medical Director

2) Rosalind Petrakova, NP
Clinical Nurse Manager

3) Maren Culbrith, RN
Aesthetic Nurse Specialist

4) Talia Verhoeven, RN

5) Dana Ostrowe, L.E.
Senior Licensed Esthetician

Target Market(s)

22-55 Females

Industry/Entity Type

Medical Spa and Wellness

Contact Information for Business Card

Logo, address, phone, web, instagram, providers name

Requirements
Must have
• Attractive classy modern look

```html
<!DOCTYPE html>
<html lang="en">
<head>
<meta charset="utf-8">
<title>Vernalis Medical Business Card</title>
<link href="https://fonts.googleapis.com/css2?family=Cinzel:wght@400&family=Montserrat:wght@500;700&display=swap" rel="stylesheet">
<style>
  :root {
    --page: #e9e9e9;
    --teal: #154f62;
    --ink: #161616;
    --black: #1a1a1a;
    --white: #ffffff;
    --photo-light: #fbf8f6;
    --photo-skin: #f1e4de;
    --photo-hair: #d9c6b8;
  }
  * { margin: 0; padding: 0; box-sizing: border-box; }
  html, body { width: 1160px; height: 1200px; overflow: hidden; background: var(--page); }
  .canvas { position: relative; width: 1160px; height: 1200px; }

  .card { position: absolute; left: 199px; width: 778px; height: 442px; overflow: hidden; }
  .card-front { top: 105px; background: var(--white); }
  .card-back { top: 634px; background: var(--teal); }

  .photo-area {
    position: absolute; left: 0; top: 0; width: 100%; height: 414px;
    background:
      radial-gradient(ellipse 170px 210px at 52% 52%, var(--photo-skin), transparent 75%),
      radial-gradient(ellipse 330px 260px at 55% 55%, var(--photo-hair), transparent 80%),
      linear-gradient(90deg, var(--photo-light) 0%, var(--photo-light) 30%, #f5ede8 60%, var(--photo-light) 100%);
    opacity: 0.85;
  }

  .footer-band { position: absolute; left: 0; top: 414px; width: 100%; height: 28px; }
  .footer-band .dark { position: absolute; left: 0; top: 0; width: 142px; height: 100%; background: var(--black); }
  .footer-band .accent { position: absolute; left: 148px; top: 0; right: 0; height: 100%; background: var(--teal); }

  .provider { position: absolute; left: 32px; top: 36px; font-family: "Montserrat", sans-serif; }
  .provider-name { font-weight: 700; font-size: 22px; letter-spacing: 0.8px; color: var(--teal); line-height: 28px; }
  .provider-role { font-weight: 500; font-size: 19.5px; letter-spacing: 1px; color: var(--ink); line-height: 27.5px; }

  .brand-small { position: absolute; right: 34px; top: 34px; width: 210px; text-align: center; font-family: "Cinzel", serif; color: var(--teal); }
  .brand-small .brand-name { font-size: 30px; letter-spacing: 4px; line-height: 36px; }
  .brand-small .brand-tagline { font-size: 9.5px; letter-spacing: 0.3px; margin-top: 6px; }
  .brand-small .brand-city { font-size: 7px; letter-spacing: 4px; margin-top: 5px; }

  .contact-list { position: absolute; left: 29px; top: 305px; list-style: none; font-family: "Montserrat", sans-serif; font-weight: 500; font-size: 19.5px; color: var(--ink); }
  .contact-list li { display: flex; align-items: center; height: 31px; }
  .contact-list svg { width: 21px; height: 21px; margin-right: 10px; flex: none; }

  .address { position: absolute; right: 29px; top: 308px; text-align: right; font-style: normal; font-family: "Montserrat", sans-serif; font-weight: 500; font-size: 19.5px; letter-spacing: 1px; line-height: 27.5px; color: var(--ink); }

  .brand-large { position: absolute; left: 0; right: 0; top: 130px; text-align: center; font-family: "Cinzel", serif; color: var(--white); }
  .brand-large .brand-name { font-size: 80px; letter-spacing: 16px; line-height: 90px; padding-left: 16px; }
  .brand-large .brand-tagline { font-size: 26px; letter-spacing: 1px; margin-top: 14px; }
  .brand-large .brand-city { font-size: 17px; letter-spacing: 12px; margin-top: 18px; padding-left: 12px; }
</style>
</head>
<body>
<main class="canvas">
  <section class="card card-front">
    <div class="photo-area" role="img" aria-label="Soft, faded photograph of a woman receiving a facial aesthetic treatment"></div>

    <div class="provider">
      <p class="provider-name">DR. DEREK HALTSWORTH</p>
      <p class="provider-role">Aesthetics and Wellness Specialist</p>
      <p class="provider-role">Medical Director</p>
    </div>

    <div class="brand-small">
      <p class="brand-name">vernalis</p>
      <p class="brand-tagline">MEDICAL AESTHETICS AND WELLNESS</p>
      <p class="brand-city">NEW YORK</p>
    </div>

    <ul class="contact-list">
      <li>
        <svg viewBox="0 0 24 24" aria-hidden="true"><path fill="#154f62" d="M3 9c0-3 4-5 9-5s9 2 9 5v2h-5V9c-1-.6-2.5-1-4-1s-3 .4-4 1v2H3z M6 12h12l2 8H4z"/></svg>
        (555)294-7051
      </li>
      <li>
        <svg viewBox="0 0 24 24" aria-hidden="true"><circle cx="12" cy="12" r="10" fill="#154f62"/></svg>
        @vernalis_medical
      </li>
      <li>
        <svg viewBox="0 0 24 24" aria-hidden="true"><circle cx="12" cy="12" r="10" fill="#154f62"/><path d="M2 12h20M12 2c-3 3-3 17 0 20M12 2c3 3 3 17 0 20" stroke="#fff" stroke-width="1.4" fill="none"/></svg>
        www.Vernalismedical-example.com
      </li>
    </ul>

    <address class="address">
      412 Harlow Brook<br>Road Suite 318<br>Ashcombe, New York 11583
    </address>

    <div class="footer-band"><span class="dark"></span><span class="accent"></span></div>
  </section>

  <section class="card card-back">
    <div class="brand-large">
      <p class="brand-name">vernalis</p>
      <p class="brand-tagline">MEDICAL AESTHETICS AND WELLNESS</p>
      <p class="brand-city">NEW YORK</p>
    </div>
  </section>
</main>
</body>
</html>
```